I work in creative/artistic projects across different mediums.
It needs to communicate creativity, style, sexy, uniqueness, individuality and sophistication.
It should not look corporate.
Colours I like are black silver gold deep purple, chocolate, orchid.
It doesn't have to make use of all these colours.
I do not like bright primary colors.
Updates

Project Deadline Extended
Reason: Still in the communication process and to allow the person enough time to finish the design. Though i should know in the next day or two. Thank you.

Target Market(s)

creatives and companies wanting to inject creativity into thier business.

Industry/Entity Type

Work

Contact Information for Business Card

Lionel Crowthwick
0418359026
lionel@lionelcrowthwick.com

quietsilverhour.com.au

Requirements
Should not have
• Anything corporate OR OLD FASHIONED

```html
<!DOCTYPE html>
<html lang="en">
<head>
<meta charset="utf-8">
<title>Lionel Crowthwick — Business Card</title>
<link rel="stylesheet" href="https://fonts.googleapis.com/css2?family=Questrial&family=Didact+Gothic&display=swap">
<style>
  :root {
    --backdrop: #e8e5e1;
    --card-black: #0b0a0a;
    --card-black-soft: #1c1a19;
    --chocolate-deep: #6e4a2e;
    --chocolate: #9a6c45;
    --band-phone: #b08a66;
    --band-mail: #cbad8c;
    --band-web: #dcc6a6;
    --band-rule: #3b3835;
    --gold: #c8a05a;
    --ink-light: #ffffff;
    --ornament: #3a3633;
  }
  html, body {
    margin: 0;
    width: 1200px;
    height: 1023px;
    overflow: hidden;
    background: var(--backdrop);
  }
  .business-card {
    position: absolute;
    left: 110px;
    top: 231px;
    width: 980px;
    height: 560px;
    box-shadow: 0 18px 40px rgba(0,0,0,0.28);
  }
  .business-card svg { display: block; }
  .contact-text {
    font-family: "Didact Gothic", "Questrial", sans-serif;
    font-size: 20px;
    fill: var(--ink-light);
    letter-spacing: 0.3px;
  }
  .holder-name {
    font-family: "Questrial", sans-serif;
    font-size: 46px;
    font-weight: 700;
    fill: var(--ink-light);
    letter-spacing: 0.5px;
  }
  .holder-role {
    font-family: "Questrial", sans-serif;
    font-size: 28px;
    fill: var(--gold);
    letter-spacing: 0.5px;
  }
  .icon { fill: var(--ink-light); }
  .icon-line { fill: none; stroke: var(--band-phone); stroke-width: 1.6; }
</style>
</head>
<body>
<div class="business-card">
  <svg width="980" height="560" viewBox="0 0 980 560" xmlns="http://www.w3.org/2000/svg">
    <defs>
      <clipPath id="card-shape"><rect width="980" height="560"/></clipPath>
      <radialGradient id="chocolate-fill" cx="0.2" cy="0.75" r="0.6">
        <stop offset="0" stop-color="var(--chocolate-deep)"/>
        <stop offset="1" stop-color="var(--chocolate)"/>
      </radialGradient>
      <radialGradient id="ornament-fill" cx="0.5" cy="0.5" r="0.5">
        <stop offset="0" stop-color="var(--ornament)" stop-opacity="0.7"/>
        <stop offset="1" stop-color="var(--ornament)" stop-opacity="0"/>
      </radialGradient>
      <path id="arc-phone" d="M 70 403 A 420 420 0 0 1 460 573"/>
      <path id="arc-mail" d="M 70 322.5 A 500 500 0 0 1 460 453"/>
      <path id="arc-web" d="M 70 237 A 585 585 0 0 1 460 344"/>
    </defs>

    <g clip-path="url(#card-shape)">
      <rect class="card-base" width="980" height="560" fill="var(--card-black)"/>

      <ellipse class="swirl-ornament" role="img" aria-label="Fine silver swirl ornament behind the name"
               cx="780" cy="170" rx="190" ry="120" fill="url(#ornament-fill)"/>

      <g class="contact-bands">
        <circle cx="120" cy="820" r="630" fill="var(--band-web)" stroke="var(--band-rule)" stroke-width="3"/>
        <circle cx="120" cy="820" r="540" fill="var(--band-mail)" stroke="var(--band-rule)" stroke-width="3"/>
        <circle cx="120" cy="820" r="460" fill="var(--band-phone)" stroke="var(--band-rule)" stroke-width="3"/>
        <circle cx="120" cy="820" r="380" fill="url(#chocolate-fill)" stroke="var(--band-rule)" stroke-width="3"/>
      </g>

      <g class="contact-icons">
        <path class="icon phone-icon" transform="translate(30 410) rotate(-20)"
              d="M-9 -14 q-4 0 -4 5 q0 12 9 20 q8 7 16 5 q3 -1 3 -4 l-1 -4 q-1 -2 -4 -1 l-4 2 q-6 -3 -9 -11 l3 -3 q1 -2 0 -4 l-3 -4 q-1 -1 -6 -1 z"/>
        <g class="mail-icon" transform="translate(30 328)">
          <rect class="icon" x="-15" y="-10" width="30" height="20" rx="1"/>
          <path class="icon-line" style="stroke: var(--band-mail)" d="M-15 -10 L0 3 L15 -10 M-15 10 L-4 0 M15 10 L4 0"/>
        </g>
        <g class="web-icon" transform="translate(30 242)">
          <circle class="icon" r="14"/>
          <path class="icon-line" style="stroke: var(--band-web)" d="M-14 0 H14 M0 -14 V14 M-11 -8 H11 M-11 8 H11"/>
          <ellipse class="icon-line" style="stroke: var(--band-web)" rx="6" ry="14"/>
        </g>
      </g>

      <g class="contact-lines">
        <text class="contact-text" dy="7"><textPath href="#arc-phone">041 835 9026</textPath></text>
        <text class="contact-text" dy="7"><textPath href="#arc-mail">lionel@lionelcrowthwick.com</textPath></text>
        <text class="contact-text" dy="7"><textPath href="#arc-web">www.quietsilverhour.com.au</textPath></text>
      </g>

      <g class="holder">
        <text class="holder-name" x="940" y="218" text-anchor="end">Lionel Crowthwick</text>
        <text class="holder-role" x="940" y="262" text-anchor="end">Creative consultant</text>
      </g>
    </g>
  </svg>
</div>
</body>
</html>
```